7 P's for Healthcare Companies - Textbook Graphic

Can you create a graphic for me for a medical textbook? The goal is to show 7 critical features of a healthcare startup and the audience is physicians with limited business backgrounds.

Please include a picture of young, male emergency physician in the middle of the graphic. Show them evaluating an idea. Can you surround the physician with bold writing for the seven components, and use brief descriptions and simple images or graphics to illustrate the point?

The image should be somewhat formal, but it's OK to be lighthearded.

The seven P's and brief descriptions include the following:
Product: what is their market solution?
(Intellectual) Property: do they have a patent or trademark?
Product Clearance: how will they get KLN approval and TPR clearance?
Payment: how will they make money?
Pilots: have they applied their product in a healthcare setting?
Physician and Patient feedback: Do doctors and patients like their product?
Publication: do they have evidence their product works?

More detail and information is available at this website: https://quvenlo.com/blog/uncategorized/healthcare-framework/

I will need to own this image

```html
<!DOCTYPE html>
<html lang="en">
<head>
<meta charset="utf-8">
<title>7P – Critical Features of a Healthcare Startup</title>
<link rel="stylesheet" href="https://fonts.googleapis.com/css2?family=Oswald:wght@300;500;600;700&family=Bebas+Neue&family=Roboto:wght@300;400&display=swap">
<style>
  :root{
    --blue:#1515f2;
    --navy:#0b0b8a;
    --ink:#111111;
    --grey:#7a7f86;
    --white:#ffffff;
  }
  html,body{margin:0;padding:0;overflow:hidden;background:var(--white);}
  .canvas{position:relative;width:1200px;height:1200px;overflow:hidden;background:var(--white);font-family:"Roboto",Arial,sans-serif;}
  .ring{position:absolute;left:0;top:0;width:1200px;height:1200px;}
  .wedge-label{font-family:"Oswald",Arial,sans-serif;font-weight:500;font-size:15px;fill:var(--white);text-anchor:middle;letter-spacing:.3px;}
  .wedge-label.light{font-weight:300;}
  .icon{fill:none;stroke:var(--white);stroke-width:2.6;stroke-linecap:round;stroke-linejoin:round;}
  .hub-number{font-family:"Bebas Neue",Arial,sans-serif;font-size:92px;fill:var(--navy);text-anchor:middle;}
  .hub-title{font-family:"Bebas Neue",Arial,sans-serif;font-size:37px;fill:var(--ink);text-anchor:middle;letter-spacing:.5px;}

  .feature{position:absolute;display:flex;align-items:flex-start;gap:8px;}
  .feature.left{flex-direction:row;text-align:right;}
  .feature.right{text-align:left;}
  .feature-number{font-family:"Bebas Neue",Arial,sans-serif;font-size:58px;line-height:46px;color:var(--blue);}
  .feature-title{font-family:"Oswald",Arial,sans-serif;font-weight:600;font-size:15px;line-height:18px;color:var(--blue);text-transform:uppercase;}
  .feature-title .soft{font-weight:500;}
  .feature-text{font-family:"Roboto",Arial,sans-serif;font-weight:300;font-size:14px;line-height:17px;color:var(--grey);}

  .physician{position:absolute;left:492px;top:648px;width:196px;height:286px;border-radius:90px 90px 6px 6px;background:linear-gradient(180deg,#d9cbbd 0%,#e9ecef 38%,#f4f5f7 70%,#dfe3e8 100%);}
  .brand{position:absolute;left:676px;top:894px;display:flex;align-items:center;gap:6px;font-family:"Oswald",Arial,sans-serif;font-weight:700;font-size:24px;color:var(--ink);}
  .brand-square{width:14px;height:14px;background:var(--blue);}
</style>
</head>
<body>
<main class="canvas">
  <svg class="ring" viewBox="0 0 1200 1200" aria-hidden="true">
    <!-- wheel -->
    <circle cx="600" cy="578" r="284" fill="var(--blue)"/>
    <circle cx="600" cy="578" r="160" fill="var(--navy)"/>
    <g stroke="var(--white)" stroke-width="11">
      <line x1="600" y1="578" x2="721" y2="285"/>
      <line x1="600" y1="578" x2="893" y2="457"/>
      <line x1="600" y1="578" x2="893" y2="699"/>
      <line x1="600" y1="578" x2="721" y2="871"/>
      <line x1="600" y1="578" x2="479" y2="871"/>
      <line x1="600" y1="578" x2="307" y2="699"/>
      <line x1="600" y1="578" x2="307" y2="457"/>
      <line x1="600" y1="578" x2="479" y2="285"/>
    </g>
    <path d="M600 578 L721 871 A300 300 0 0 1 479 871 Z" fill="var(--white)"/>
    <!-- hub cross -->
    <rect x="539" y="422" width="122" height="460" fill="var(--white)"/>
    <rect x="443" y="539" width="314" height="104" fill="var(--white)"/>

    <text class="hub-number" x="600" y="512">7P</text>
    <text class="hub-title" x="600" y="585">CRITICAL FEATURES OF</text>
    <text class="hub-title" x="600" y="622">A HEALTHCARE STARTUP</text>

    <!-- Intellectual property -->
    <g transform="translate(600 343)">
      <rect class="icon" x="-20" y="-17" width="40" height="30" rx="2"/>
      <line class="icon" x1="-12" y1="-8" x2="12" y2="-8"/>
      <line class="icon" x1="-12" y1="-1" x2="6" y2="-1"/>
      <circle class="icon" cx="8" cy="12" r="6"/>
      <path class="icon" d="M5 17 L4 24 L8 21 L12 24 L11 17"/>
    </g>
    <text class="wedge-label light" x="600" y="389">INTELLECTUAL</text>
    <text class="wedge-label" x="600" y="408">PROPERTY</text>

    <!-- Pilots -->
    <g transform="translate(441 418)">
      <path class="icon" d="M-3 -14 C-3 -22 -14 -22 -14 -12 C-14 -4 -3 2 -3 2 C-3 2 8 -4 8 -12 C8 -22 -3 -22 -3 -14 Z"/>
      <line class="icon" x1="10" y1="-20" x2="10" y2="-10"/>
      <line class="icon" x1="5" y1="-15" x2="15" y2="-15"/>
      <path class="icon" d="M-20 8 H-12 C-6 8 -2 12 4 12 H10 M-2 16 H14 L20 10"/>
      <rect class="icon" x="-24" y="5" width="5" height="16"/>
    </g>
    <text class="wedge-label" x="441" y="459">PILOTS</text>

    <!-- Payment -->
    <g transform="translate(753 414)">
      <rect class="icon" x="-10" y="-20" width="30" height="18" rx="2"/>
      <circle class="icon" cx="5" cy="-11" r="4"/>
      <path class="icon" d="M-20 8 H-12 C-6 8 -2 12 4 12 H10 M-2 16 H14 L20 10"/>
      <rect class="icon" x="-24" y="5" width="5" height="16"/>
    </g>
    <text class="wedge-label" x="753" y="458">PAYMENT</text>

    <!-- Physician & patient feedback -->
    <g transform="translate(818 545)">
      <rect class="icon" x="-18" y="-2" width="7" height="20"/>
      <path class="icon" d="M-11 0 L-4 -8 L-2 -18 C2 -18 4 -14 3 -8 H12 C15 -8 16 -5 15 -2 L12 14 C11 17 9 18 6 18 H-11"/>
      <circle class="icon" cx="12" cy="-18" r="8"/>
      <path class="icon" d="M8 -18 L11 -15 L16 -21"/>
    </g>
    <text class="wedge-label" x="818" y="589">PHYSICIAN</text>
    <text class="wedge-label" x="818" y="608">&amp; PATIENT</text>
    <text class="wedge-label" x="818" y="627">FEEDBACK</text>

    <!-- Publication -->
    <g transform="translate(753 720)">
      <path class="icon" d="M-14 -20 H6 L14 -12 V18 H-14 Z"/>
      <line class="icon" x1="-8" y1="-10" x2="4" y2="-10"/>
      <line class="icon" x1="-8" y1="-3" x2="6" y2="-3"/>
      <line class="icon" x1="-8" y1="4" x2="0" y2="4"/>
      <path class="icon" d="M12 2 L20 5 V12 C20 17 16 20 12 22 C8 20 4 17 4 12 V5 Z"/>
      <path class="icon" d="M8 11 L11 14 L16 8"/>
    </g>
    <text class="wedge-label" x="753" y="765">PUBLICATION</text>

    <!-- Product -->
    <g transform="translate(431 716)">
      <path class="icon" d="M0 -9 L9 -4 V6 L0 11 L-9 6 V-4 Z"/>
      <circle class="icon" cx="0" cy="-20" r="3.5"/>
      <circle class="icon" cx="-19" cy="-10" r="3.5"/>
      <circle class="icon" cx="19" cy="-10" r="3.5"/>
      <circle class="icon" cx="-19" cy="16" r="3.5"/>
      <circle class="icon" cx="19" cy="16" r="3.5"/>
      <line class="icon" x1="0" y1="-16" x2="0" y2="-9"/>
      <line class="icon" x1="-16" y1="-8" x2="-9" y2="-4"/>
      <line class="icon" x1="16" y1="-8" x2="9" y2="-4"/>
      <line class="icon" x1="-16" y1="14" x2="-9" y2="6"/>
      <line class="icon" x1="16" y1="14" x2="9" y2="6"/>
    </g>
    <text class="wedge-label" x="431" y="760">PRODUCT</text>

    <!-- Product clearance -->
    <g transform="translate(373 543)">
      <path class="icon" d="M0 -20 L6 -15 L14 -16 L15 -8 L20 -2 L15 5 L14 13 L6 12 L0 17 L-6 12 L-14 13 L-15 5 L-20 -2 L-15 -8 L-14 -16 L-6 -15 Z" fill="var(--white)" stroke="var(--white)"/>
      <path d="M-7 -1 L-2 4 L8 -6" fill="none" stroke="var(--blue)" stroke-width="3.5" stroke-linecap="round" stroke-linejoin="round"/>
    </g>
    <text class="wedge-label" x="373" y="589">PRODUCT</text>
    <text class="wedge-label" x="373" y="607">CLEARANCE</text>
  </svg>

  <div class="physician" role="img" aria-label="Photo of a young male emergency physician in a white coat with a stethoscope, holding a tablet while evaluating an idea"></div>
  <div class="brand"><span class="brand-square"></span>quvenlo</div>

  <!-- left column -->
  <div class="feature left" style="right:926px;top:356px;">
    <div>
      <div class="feature-title">Pilots</div>
      <div class="feature-text">Have they applied their product<br>in a healthcare setting?</div>
    </div>
  </div>
  <div class="feature-number" style="position:absolute;left:278px;top:356px;">3</div>

  <div class="feature left" style="right:936px;top:563px;">
    <div>
      <div class="feature-title">Product Clearance</div>
      <div class="feature-text">How will they get KLN approval<br>and TPR clearance?</div>
    </div>
  </div>
  <div class="feature-number" style="position:absolute;left:272px;top:562px;">2</div>

  <div class="feature left" style="right:933px;top:775px;">
    <div>
      <div class="feature-title">Product</div>
      <div class="feature-text">What is their market solution?</div>
    </div>
  </div>
  <div class="feature-number" style="position:absolute;left:280px;top:776px;">1</div>

  <!-- top -->
  <div class="feature right" style="left:500px;top:240px;">
    <div class="feature-number">4</div>
    <div>
      <div class="feature-title"><span class="soft">Intellectual</span> Property</div>
      <div class="feature-text">Do they have a patent or trademark?</div>
    </div>
  </div>

  <!-- right column -->
  <div class="feature right" style="left:886px;top:358px;">
    <div class="feature-number">5</div>
    <div>
      <div class="feature-title">Payment</div>
      <div class="feature-text">How will they make money?</div>
    </div>
  </div>

  <div class="feature right" style="left:886px;top:566px;">
    <div class="feature-number">6</div>
    <div>
      <div class="feature-title">Physician &amp; Patient Feedback</div>
      <div class="feature-text">Do doctors and patients<br>like their product?</div>
    </div>
  </div>

  <div class="feature right" style="left:886px;top:775px;">
    <div class="feature-number">7</div>
    <div>
      <div class="feature-title">Publication</div>
      <div class="feature-text">Do they have evidence<br>their product works?</div>
    </div>
  </div>
</main>
</body>
</html>
```